Health and Wellness Company Business Card

I need a business card design that is clean and uses modern minimalist style. The design should incorporate our logo (see attached). I would also like to use embossing on the cards so that they also have a great feel. I am open to the card using one or more colors, and these do not have to correspond to the colors in the concept paper. The card can either be one-sided or use both sides of the card.The logo uses the Avenir font.

I will need the file designed in Adobe CS and compatible with CS5.5 (Illustrator preferable) and I'll need the working file (for example: .ai) once the project is complete so that I can change the names/contact info/etc for each variation of the card.

This needs to be a memorable card for the recipient. They should think: "This is a great business card" either because of its simplicity or embossing effects or use of color.

Target Market(s)

The audience for our company has two main groups: people who pay for healthcare (insurers, companies, researcher companies) and people with chronic health conditions who are the consumers of our services and resources.

Industry/Entity Type

Business

Requirements
Must have
• Essential components of the card include: Company logo, contact Name (Mark Dalton), phone number (5049381726), email address (mdalton@brevolin.com), slogan/tagline that consists of ~30-40 characters (Use Lorem Ipsum)
Nice to have
• These fall just slightly short of "must have" to allow for design flexibility: Embossing or spot varnish effects and a splash of color
Should not have
• Designs with these components will not be successful: flashy or showy designs that are not professional in appearance, and lots of different colors

```html
<!DOCTYPE html>
<html lang="en">
<head>
<meta charset="utf-8">
<title>Brevolin Bi-Fold Business Card</title>
<link rel="stylesheet" href="https://fonts.googleapis.com/css2?family=Arimo:ital,wght@0,400;0,700;1,400&family=Open+Sans:wght@400;600&display=swap">
<style>
  :root {
    --sheet: #ffffff;
    --sheet-edge: #9a9a9a;
    --ink: #1e1e1e;
    --slate: #7a7f8d;
    --mist: #dcdcdc;
    --mist-inside: #dfdfdf;
    --card-text: #8a8f9b;
    --white: #ffffff;
  }
  html, body { margin: 0; padding: 0; width: 1001px; height: 1200px; overflow: hidden; background: var(--sheet); }
  .sheet {
    position: relative; width: 933px; height: 1118px;
    transform: scale(1.0729, 1.0733); transform-origin: 0 0;
    font-family: "Open Sans", sans-serif;
  }
  .sheet-frame { position: absolute; inset: 0; border: 1px solid var(--sheet-edge); box-sizing: border-box; }
  .shapes { position: absolute; left: 0; top: 0; }
  .note { position: absolute; margin: 0; font-family: "Arimo", sans-serif; color: var(--ink); white-space: nowrap; }
  .title { left: 467px; top: 26px; font-size: 22px; }
  .fold-label { left: 348px; top: 41px; font-size: 21px; font-style: italic; }
  .features { left: 27px; top: 143px; font-size: 20px; font-style: italic; line-height: 39px; }
  .section-label { font-size: 17px; }
  .label-inside { left: 90px; top: 383px; }
  .label-back { left: 93px; top: 734px; }

  .t { position: absolute; margin: 0; white-space: nowrap; color: var(--card-text); }
  .name { font-size: 17px; }
  .company { font-size: 18px; }
  .contact { font-size: 13px; line-height: 19.5px; letter-spacing: 0.3px; }
  .brand-name {
    position: absolute; margin: 0; color: var(--white); font-weight: 600;
    font-size: 21px; letter-spacing: 6px; white-space: nowrap;
  }
  .about {
    position: absolute; left: 110px; top: 892px; width: 470px; margin: 0;
    color: var(--white); font-size: 14px; font-weight: 600; line-height: 25px; text-align: center;
  }
  .tagline {
    position: absolute; left: 110px; top: 1018px; width: 470px; margin: 0;
    color: var(--white); font-family: "Arimo", sans-serif; font-weight: 700; font-size: 15px; text-align: center;
  }
</style>
</head>
<body>
<div class="sheet">
  <div class="sheet-frame"></div>

  <svg class="shapes" width="933" height="1118" viewBox="0 0 933 1118" aria-hidden="true">
    <rect class="closed-card" x="376" y="66" width="545" height="300" fill="var(--mist)" stroke="#555" stroke-width="1"/>
    <path class="closed-cover" d="M376,140 A74,74 0 0 1 450,66 L666,66 L666,286 A80,80 0 0 1 586,366 L376,366 Z" fill="var(--slate)"/>
    <path class="fold-arrow" d="M375,80 L379,80 L379,104 L383,104 L377,115 L371,104 L375,104 Z" fill="none" stroke="#333" stroke-width="1"/>
    <path class="inside-card" d="M86,414 L893,414 L893,714 L200,714 A114,114 0 0 1 86,600 Z" fill="var(--mist-inside)"/>
    <path class="back-panel" d="M86,763 L520,763 A83,83 0 0 1 603,846 L603,1062 L86,1062 Z" fill="var(--slate)" stroke="#333" stroke-width="1"/>
    <path class="front-panel" d="M604,846 A83,83 0 0 1 687,763 L893,763 L893,1000 A62,62 0 0 1 831,1062 L604,1062 Z" fill="var(--slate)"/>
  </svg>

  <p class="note title">CLOSED BI FOLD BUSINESS CARD</p>
  <p class="note fold-label">FOLD</p>
  <p class="note features">Business Card features :<br>* Both side Matt Lamination<br>* Embossing work on LOGO<br>* Speacialized Die Cut Card</p>

  <p class="brand-name" style="left:423px; top:276px;">BREVOLIN</p>
  <p class="t name" style="left:770px; top:104px;">Mark Dalton</p>
  <p class="t company" style="left:693px; top:255px;">Brevolin Health Inc.</p>
  <p class="t contact" style="left:693px; top:283px;">a : ################<br>p : 5049381726<br>e : mdalton@brevolin.com</p>

  <p class="note section-label label-inside">INSIDE OF OPEN CARD</p>
  <p class="t name" style="left:770px; top:451px;">Mark Dalton</p>
  <p class="t company" style="left:693px; top:601px;">Brevolin Health Inc.</p>
  <p class="t contact" style="left:693px; top:629px;">a : ################<br>p : 5049381726<br>e : mdalton@brevolin.com</p>

  <p class="note section-label label-back">BACK OF OPEN CARD</p>
  <p class="about">Brevolin Health Inc. is an online, member-led approach to wellness through learning, open conversation, and daily habit support for people living with chronic joint pain.</p>
  <p class="tagline">Move, Connect, &amp; Thrive</p>
  <p class="brand-name" style="left:650px; top:966px;">BREVOLIN</p>
</div>
</body>
</html>
```